Rovilent.com Trucking Company Website

Need a website designed (no content) for a trucking company, specializing in trucking of ocean containers (intermodal Trucking). Heavy emphasis on technology, using latest technology, providing unabated visibility and realtime information.
clean minimalist industrial website
example:
https://www.belquarn.com/

Target Market(s)

Professional Business Consumer corporate and small business

Industry/Entity Type

Trucking Company

Number of Pages Required

5+ page

Requirements
Must have
• Industrial Design, simple informative, for a busy professional to view and get the necessary information with out the distractions.
• Blog Page
• Client Log-In on the front page
• Technology page - showing our intensive investments in technology
Nice to have
• If ANY images included, MUST be USA related. Example if include an image of a truck, ensure its a USA model. Do the research.
• included our business card for sample of Logo
• Doesnt not have to be the same color schemes.
Should not have
• moving images

```html
<!DOCTYPE html>
<html lang="en">
<head>
<meta charset="utf-8">
<title>Rovilent Consulting – Intermodal Trucking</title>
<link href="https://fonts.googleapis.com/css2?family=Lato:ital,wght@0,400;0,700;1,700&family=Raleway:wght@400;500;600;700&display=swap" rel="stylesheet">
<style>
:root{
  --brand-blue:#0d4f94;
  --button-blue:#0b4a8a;
  --ink:#2b2b2b;
  --text-grey:#3a3a3a;
  --tagline-grey:#444;
  --caption-dark:#15191d;
  --footer-black:#000;
  --divider:#cfd3d6;
  --white:#fff;
}
*{margin:0;padding:0;box-sizing:border-box}
html,body{width:1187px;height:1200px;overflow:hidden}
body{position:relative;font-family:"Lato",sans-serif;color:var(--ink);background:#eef1f4}

.hero{position:absolute;left:0;top:0;width:1187px;height:644px}
.hero-photo{position:absolute;inset:0;
  background:
    radial-gradient(ellipse 420px 300px at 880px 300px,rgba(255,255,255,.55),rgba(255,255,255,0) 70%),
    linear-gradient(90deg,#8ea9c0 0%,#2a2f36 7%,#1d2126 40%,#6f8ea9 55%,#a9c6db 75%,#8fb0cb 100%)}
.phone-line{position:absolute;right:103px;top:9px;font-size:17px;font-weight:700;color:#34404c;display:flex;align-items:center;gap:8px}
.site-header{position:absolute;left:97px;top:42px;width:993px;height:94px;background:var(--white);border-radius:13px;box-shadow:0 2px 6px rgba(0,0,0,.15)}
.brand-name{position:absolute;left:22px;top:22px;font-family:"Raleway",sans-serif;font-weight:700;color:var(--brand-blue);font-size:30px;line-height:1;letter-spacing:1px}
.brand-name small{display:block;font-size:15px;letter-spacing:6px;margin-top:6px}
.main-nav{position:absolute;right:30px;top:0;height:94px;display:flex;align-items:center}
.nav-item{display:flex;align-items:center;gap:9px;font-family:"Raleway",sans-serif;font-size:16px;color:#222;padding:0 38px;height:46px;border-left:1px solid #e3e3e3}
.nav-item:first-child{border-left:none}
.nav-item:last-child{padding-right:0}
.hero-caption{position:absolute;left:469px;top:491px;width:621px;height:82px;background:var(--caption-dark);color:var(--white);font-family:"Raleway",sans-serif;font-weight:700;font-size:30px;display:flex;align-items:center;justify-content:center;letter-spacing:.3px}
.know-more{position:absolute;left:983px;top:581px;width:102px;height:32px;background:var(--button-blue);color:var(--white);font-style:italic;font-weight:700;font-size:16px;display:flex;align-items:center;justify-content:center}

.services{position:absolute;left:0;top:644px;width:1187px;height:505px}
.services-photo{position:absolute;inset:0;background:linear-gradient(100deg,#f8f1ec 0%,#f3ece8 35%,#e9edf1 60%,#eef1f4 100%)}
.intro{position:absolute;left:97px;top:146px;width:374px;text-align:center}
.intro-name{font-family:"Raleway",sans-serif;font-weight:700;color:var(--brand-blue);font-size:56px;line-height:1;letter-spacing:2px}
.intro-name span{display:block;font-size:31px;letter-spacing:9px;margin-top:8px}
.tagline{margin-top:22px;font-size:21px;line-height:31px;color:var(--tagline-grey)}
.service-list{position:absolute;left:574px;top:43px;width:520px;height:423px;border-left:2px solid var(--divider)}
.service{position:absolute;left:0;width:520px}
.service::before{content:"";position:absolute;left:-2px;top:0;width:2px;height:80px;background:var(--brand-blue)}
.service::after{content:"";position:absolute;left:0;top:34px;border-left:5px solid var(--brand-blue);border-top:6px solid transparent;border-bottom:6px solid transparent}
.service-head{display:flex;align-items:center;gap:20px;padding-left:22px;height:40px}
.service-head h2{font-family:"Raleway",sans-serif;font-weight:600;font-size:21px;color:#333}
.service p{padding-left:22px;font-size:14px;line-height:19px;color:var(--text-grey);margin-top:6px}

.site-footer{position:absolute;left:0;top:1149px;width:1187px;height:51px;background:var(--footer-black);color:var(--white);font-size:14px;display:flex;align-items:center;justify-content:center}
</style>
</head>
<body>
<section class="hero">
  <div class="hero-photo" role="img" aria-label="Businessman in a dark suit touching a glowing world map network on a light blue background"></div>
  <div class="phone-line">
    <svg width="15" height="15" viewBox="0 0 24 24"><path fill="#34404c" d="M6.6 10.8a15 15 0 0 0 6.6 6.6l2.2-2.2c.3-.3.7-.4 1-.2 1.1.4 2.3.6 3.6.6.6 0 1 .4 1 1V20c0 .6-.4 1-1 1A17 17 0 0 1 3 4c0-.6.4-1 1-1h3.5c.6 0 1 .4 1 1 0 1.3.2 2.5.6 3.6.1.3 0 .7-.2 1z"/></svg>
    Call Now : 555-014-2290
  </div>
  <header class="site-header">
    <div class="brand-name">ROVILENT<small>CONSULTING</small></div>
    <nav class="main-nav">
      <div class="nav-item">
        <svg width="20" height="20" viewBox="0 0 20 20"><rect width="20" height="20" rx="5" fill="#222"/><rect x="5" y="6" width="6" height="2.5" rx="1" fill="#fff"/><rect x="5" y="11.5" width="10" height="2.5" rx="1" fill="#fff"/></svg>
        Blog</div>
      <div class="nav-item">
        <svg width="30" height="26" viewBox="0 0 30 26"><circle cx="11" cy="7" r="6" fill="#222"/><path d="M0 25c0-7 5-11 11-11s11 4 11 11z" fill="#222"/><circle cx="23" cy="19" r="6" fill="#222" stroke="#fff" stroke-width="1.5"/><circle cx="21" cy="19" r="1.5" fill="#fff"/><rect x="22" y="18.3" width="5" height="1.4" fill="#fff"/></svg>
        Client Log-In</div>
      <div class="nav-item">
        <svg width="24" height="26" viewBox="0 0 24 26"><g fill="none" stroke="#222" stroke-width="2"><circle cx="9" cy="17" r="5"/><circle cx="9" cy="17" r="1.8"/><circle cx="17" cy="6" r="3.5"/><path d="M9 10v2M9 22v2M2 17h2M14 17h2M17 1v1.5M17 9.5V11M12 6h1.5M20.5 6H22"/></g></svg>
        Technology</div>
    </nav>
  </header>
  <h1 class="hero-caption">We Are A Technology Driven Company</h1>
  <a class="know-more">Know More</a>
</section>

<section class="services">
  <div class="services-photo" role="img" aria-label="Faded photo of a white American semi truck on the highway"></div>
  <div class="intro">
    <div class="intro-name">ROVILENT<span>CONSULTING</span></div>
    <p class="tagline">We Are A Trucking Business Specializing In Trucking Of Ocean Containers</p>
  </div>
  <div class="service-list">
    <article class="service" style="top:5px">
      <div class="service-head">
        <svg width="30" height="36" viewBox="0 0 30 36"><g fill="#333"><rect x="4" y="2" width="22" height="6" rx="2"/><rect x="2" y="9" width="26" height="16" rx="2"/><rect x="3" y="26" width="6" height="8"/><rect x="21" y="26" width="6" height="8"/></g><rect x="6" y="12" width="18" height="6" fill="#fff"/><circle cx="7" cy="22" r="1.5" fill="#fff"/><circle cx="23" cy="22" r="1.5" fill="#fff"/></svg>
        <h2>Intermodal Trucking</h2>
      </div>
      <p>Lorem ipsum dolor sit amet, consectetur adipiscing elit, sed do eiusmod tempor incididunt ut labore et dolore magna aliqua. Ut enim ad minim veniam, quis nostrud</p>
    </article>
    <article class="service" style="top:132px">
      <div class="service-head">
        <svg width="40" height="32" viewBox="0 0 40 32"><g fill="#333"><rect x="0" y="2" width="26" height="20" rx="2"/><path d="M27 8h7l5 7v9H27z"/><circle cx="8" cy="26" r="5"/><circle cx="32" cy="26" r="5"/></g><text x="3" y="16" font-family="Lato,sans-serif" font-weight="700" font-size="11" fill="#fff">LTL</text></svg>
        <h2>LTL</h2>
      </div>
      <p>Lorem ipsum dolor sit amet, consectetur adipiscing elit, sed do eiusmod tempor incididunt ut labore et dolore magna aliqua. Ut enim ad minim veniam, quis nostrud</p>
    </article>
    <article class="service" style="top:259px">
      <div class="service-head">
        <svg width="36" height="32" viewBox="0 0 36 32"><path fill="#333" d="M0 10 18 0l18 10v22H0z"/><rect x="6" y="14" width="24" height="18" fill="#fff"/><g fill="#333"><rect x="8" y="16" width="9" height="6"/><rect x="19" y="16" width="9" height="6"/><rect x="8" y="24" width="20" height="6"/></g></svg>
        <h2>Warehousing</h2>
      </div>
      <p>Lorem ipsum dolor sit amet, consectetur adipiscing elit, sed do eiusmod tempor incididunt ut labore et dolore magna aliqua. Ut enim ad minim veniam, quis nostrud</p>
    </article>
  </div>
</section>

<footer class="site-footer">Copyright © 2017&nbsp; Rovilent Consulting&nbsp; I&nbsp; All Rights Reserved.</footer>
</body>
</html>
```